Plumbing company needs a brochure design

Korvane Building Works is a mechanical services plumbing company that designs, installs, services and maintains commercial & industrial HVAC systems (heating, ventilation, air-conditioning systems manufactured by Trelvo, Fenrok and Halberd Thermal).
We would like a brochure that could be sent to prospects following a cold or warm call as a general introduction prior to a sales appointment.
We'd like to incorporate our 'breath clean air' campaign in the brochure as well. Details are on our website
The services we'd like to focus on the following services: Air conditioning; Design; Service & Maintenance; Air Filtration; and Refrigeration. No need to mention labour hire or trades & services
Our website is korvanebuildingworks.example
Target Market(s)
Building and property managers; building owners; facility managers of restaurants; hospitals; aged care facilities; conference centres; shopping centres
Industry/Entity Type
Industrial
Requirements
Must have
- 4 pages; contact details on last page (same as listed on our 'Contact Us' page on website. Half fold

```html
<!DOCTYPE html>
<html lang="en">
<head>
<meta charset="utf-8">
<title>Korvane Building Works – Master Plumber Services</title>
<link href="https://fonts.googleapis.com/css2?family=Roboto+Condensed:wght@400;700&family=Roboto:wght@300;400&display=swap" rel="stylesheet">
<style>
  :root {
    --sky-light: #a9dcf6;
    --sky-mid: #8cc6ee;
    --sky-deep: #5d9bd6;
    --navy: #0f5b96;
    --service-blue: #1b74bf;
    --rule-blue: #2a6fb0;
    --body-grey: #5a5a5a;
    --badge-red: #c51f2e;
    --white: #ffffff;
    --frame-grey: #8d8d8d;
  }
  * { margin: 0; padding: 0; box-sizing: border-box; }
  html, body { width: 1200px; height: 848px; overflow: hidden; }
  body { background: var(--white); }
  .brochure {
    position: relative;
    width: 1200px; height: 848px; overflow: hidden;
    background: linear-gradient(125deg, var(--sky-light) 0%, var(--sky-light) 35%, var(--sky-mid) 65%, var(--sky-deep) 100%);
    font-family: "Roboto", Arial, sans-serif;
  }
  .services-title {
    position: absolute; left: 221px; top: 116px;
    font-family: "Roboto Condensed", "Arial Narrow", sans-serif;
    font-weight: 700; font-size: 52px; line-height: 1;
    color: var(--navy); letter-spacing: -0.3px;
  }
  .title-rule {
    position: absolute; left: 0; top: 171px; width: 752px; height: 1.5px;
    background: var(--rule-blue);
  }
  .service-list {
    position: absolute; left: 253px; top: 199px; width: 500px;
    list-style: none;
    font-family: "Roboto Condensed", "Arial Narrow", sans-serif;
    font-weight: 700; font-size: 17.5px; line-height: 19px;
    color: var(--service-blue);
  }
  .service-list li { margin-bottom: 14px; }
  .body-copy {
    position: absolute;
    font-weight: 400; font-size: 15.2px; line-height: 20px;
    color: var(--body-grey);
  }
  .copy-standards { left: 210px; top: 473px; width: 560px; text-align: center; }
  .copy-engineers { left: 318px; top: 533px; width: 360px; }
  .copy-company { left: 293px; top: 653px; width: 500px; }
  .copy-engineers span, .copy-company span { display: block; }
  .diagram-card {
    position: absolute; left: 28px; top: 530px; width: 280px; height: 198px;
    transform: rotate(-10deg);
    background: linear-gradient(135deg, #f4f7f9 0%, #dfe8ee 55%, #c9d6df 100%);
    border: 7px solid var(--frame-grey);
    box-shadow: 2px 3px 6px rgba(0,0,0,0.25);
  }
  .years-badge { position: absolute; left: 700px; top: 508px; width: 132px; height: 132px; }
  .fact-panel {
    position: absolute; left: 812px; top: 0; width: 340px; height: 784px;
    background: var(--navy); color: var(--white);
    text-align: center;
  }
  .fact-heading {
    margin-top: 50px;
    font-family: "Roboto Condensed", "Arial Narrow", sans-serif;
    font-weight: 400; font-size: 42px; line-height: 1;
  }
  .fact {
    position: absolute; left: 20px; width: 300px;
    font-size: 21px; line-height: 23px; font-weight: 400;
  }
  .fact-1 { top: 136px; }
  .fact-2 { top: 296px; }
  .fact-3 { top: 456px; }
  .fact-4 { top: 638px; }
</style>
</head>
<body>
<main class="brochure">
  <h1 class="services-title">Master Plumber Services:</h1>
  <div class="title-rule"></div>

  <ul class="service-list">
    <li>Project Management</li>
    <li>In-house engineered designed air-conditioning&nbsp; and chiller systems</li>
    <li>Install and commission air conditioning and chillers</li>
    <li>Service and Maintenance of air-conditioning and chiller systems</li>
    <li>Hire portable air conditioner, portable aircon, portable ac</li>
    <li>Air Filtraition - supply and fit energy efficient &amp; independently European certified air filters</li>
  </ul>

  <p class="body-copy copy-standards">Our air-conditioning systems are designed to meet the requirements of Australian Standards and best practice.</p>

  <p class="body-copy copy-engineers">
    <span style="padding-left:6px">Our in-house mechanical engineers design</span>
    <span style="padding-left:10px">HVAC (Heating, Ventilation, Air conditioning)</span>
    <span style="padding-left:14px">sysyems based on the principals of</span>
    <span style="padding-left:18px">thermodynamics, fluid mechanics and heat</span>
    <span style="padding-left:22px">transfer.</span>
  </p>

  <p class="body-copy copy-company">
    <span style="padding-left:58px">Korvane Building Works offers commercial air conditioning</span>
    <span style="padding-left:62px">supplies, installation, maintenance and repair. With over</span>
    <span style="padding-left:62px">40 years in the business of design, service and</span>
    <span>installation of commercial air conditioning system we are</span>
    <span>confident that all jobs twe do are done to the best possible</span>
    <span>standard and will lead to machines lasting longer and working</span>
    <span>more efficiently.</span>
  </p>

  <div class="diagram-card" role="img" aria-label="Cutaway diagram of a commercial building HVAC system with labelled indoor and outdoor units"></div>

  <svg class="years-badge" viewBox="0 0 132 132" aria-label="Over 40 years in the business">
    <polygon fill="var(--badge-red)" points="66,2 73,14 84,5 87,19 100,13 99,27 113,26 108,39 121,43 112,53 123,60 112,67 120,77 108,81 113,94 99,94 99,108 86,102 83,116 73,107 66,120 59,107 49,116 46,102 33,108 33,94 19,94 24,81 12,77 20,67 9,60 20,53 11,43 24,39 19,26 33,27 32,13 45,19 48,5 59,14"/>
    <g transform="rotate(-25 66 61)" fill="var(--white)" font-family="Roboto, Arial, sans-serif" text-anchor="middle">
      <text x="66" y="36" font-size="17" font-weight="300">over</text>
      <text x="66" y="70" font-size="40" font-weight="700" font-family="'Roboto Condensed', sans-serif">40</text>
      <text x="70" y="84" font-size="12" font-weight="300">years</text>
      <text x="72" y="95" font-size="12" font-weight="300">in the</text>
      <text x="74" y="106" font-size="12" font-weight="300">business</text>
    </g>
  </svg>

  <aside class="fact-panel">
    <h2 class="fact-heading">Did you know?</h2>
    <p class="fact fact-1">HVAC typically accounts for between 25-50 per cent of the total energy costs for businesses and commercial buildings.</p>
    <p class="fact fact-2">By reducing draughts via leaks, gaps and cracks, you may save up to 25 per cent of your heating and cooling costs.</p>
    <p class="fact fact-3">In summer, increasing the temperature of your air conditioning system by 1°C may reduce energy consumption and your bill by around 10 per cent.</p>
    <p class="fact fact-4">By keeping your HVAC system well maintained, you may save on air conditioning operating costs.</p>
  </aside>
</main>
</body>
</html>
```